out of the box Business Card Design for a Manufacturer / Distributor

We are a manufarturer and distributor of products.
the company name is VORTANI (Pic attached)

the picture is NOT a must have on the business Card.

the Business Card should look really professional and/or special, so out of the box thinking is welcome.

there should be 2 Adresses on the Business Card for Main and Branch Office.
Email Adress, homepage, Name is required
NO Phone Number

Our working field:
Private Labeling
high Quality Production
direct distribution
warehousing
trademark registration
legal support

Main Office:
Kornblumenweg 14
08352 Lindenfeld
Westmark

Branch Office:
Daska Lane
Ravipur
Ostavia

Names:
Lukas Feldhaus (Owner)
Imran Qureshi (Owner)

Email:
lukas@vortani-example.com
imran@vortani-example.com

homepage:
vortani-example.com

Industry/Entity Type

Manufacturer Distributer

Contact Information for Business Card

Vortani

Requirements
Must have
• Names, both office Adresses, email, homepage
Should not have
• Phone Number

```html
<!DOCTYPE html>
<html lang="en">
<head>
<meta charset="utf-8">
<title>Vortani – Business Card</title>
<link rel="stylesheet" href="https://fonts.googleapis.com/css2?family=Montserrat:wght@400;500;600&display=swap">
<style>
  :root {
    --bg: #3b3b3b;
    --card: #1a1a1a;
    --accent: #e8734d;
    --text: #f2f2f2;
    --muted: #8a8a8a;
    --rule: #555555;
  }
  * { box-sizing: border-box; margin: 0; padding: 0; }
  html, body {
    width: 1200px; height: 801px; overflow: hidden;
    background: radial-gradient(ellipse at 50% 35%, #454545 0%, var(--bg) 70%);
    font-family: "Montserrat", sans-serif;
  }
  .stage {
    position: relative; width: 1200px; height: 801px;
    display: flex; align-items: center; justify-content: center; gap: 44px;
  }
  .card {
    position: relative;
    width: 520px; height: 336px;
    background: var(--card);
    border: 2px solid var(--accent);
    box-shadow: 0 18px 40px rgba(0,0,0,0.45);
    color: var(--text);
    overflow: hidden;
  }

  /* Contact side */
  .contact { padding: 40px 40px 0 42px; }
  .person { margin-bottom: 10px; }
  .person-name {
    color: var(--accent); font-weight: 600; font-size: 19px;
    letter-spacing: 0.3px; text-transform: uppercase; line-height: 1.1;
  }
  .person-role { font-size: 13px; line-height: 1.3; }
  .emails { list-style: none; margin-top: 6px; font-size: 13.5px; line-height: 1.5; }
  .emails li { display: flex; align-items: center; gap: 8px; }
  .emails svg { width: 13px; height: 10px; flex: none; }
  .offices { display: flex; margin-top: 14px; font-size: 13.5px; line-height: 1.35; }
  .office { padding-right: 22px; font-style: normal; }
  .office + .office { padding-left: 22px; border-left: 1px solid var(--rule); }
  .office-title { color: var(--accent); font-weight: 500; }
  .website {
    position: absolute; left: 42px; bottom: 28px;
    color: var(--accent); font-weight: 500; font-size: 15px;
  }

  /* Brand side */
  .brand {
    display: flex; flex-direction: column; align-items: center;
    padding-top: 92px; text-align: center;
  }
  .brand-mark { display: flex; align-items: center; gap: 16px; }
  .brand-dot { width: 40px; height: 40px; border-radius: 50%; background: #2a2a2a; }
  .brand-name {
    font-weight: 500; font-size: 50px; letter-spacing: 3px; color: var(--muted);
  }
  .field-title {
    margin-top: 44px; color: var(--accent); font-weight: 600;
    font-size: 14px; letter-spacing: 0.5px;
  }
  .field-list { margin-top: 6px; font-size: 13.5px; line-height: 1.5; }
  .field-list .sep { color: var(--accent); margin: 0 7px; font-weight: 600; }
</style>
</head>
<body>
<main class="stage">
  <article class="card contact">
    <div class="person">
      <h2 class="person-name">Lukas Feldhaus</h2>
      <p class="person-role">Owner</p>
    </div>
    <div class="person">
      <h2 class="person-name">Imran Qureshi</h2>
      <p class="person-role">Owner</p>
    </div>
    <ul class="emails">
      <li><svg viewBox="0 0 13 10"><rect x="0.5" y="0.5" width="12" height="9" fill="none" stroke="#e8734d"/><path d="M0.5 0.5 L6.5 5.5 L12.5 0.5" fill="none" stroke="#e8734d"/></svg>lukas@vortani-example.com</li>
      <li><svg viewBox="0 0 13 10"><rect x="0.5" y="0.5" width="12" height="9" fill="none" stroke="#e8734d"/><path d="M0.5 0.5 L6.5 5.5 L12.5 0.5" fill="none" stroke="#e8734d"/></svg>imran@vortani-example.com</li>
    </ul>
    <div class="offices">
      <address class="office">
        <p class="office-title">Main Office:</p>
        <p>Kornblumenweg 14</p>
        <p>08352 Lindenfeld</p>
        <p>Westmark</p>
      </address>
      <address class="office">
        <p class="office-title">Branch Office:</p>
        <p>Daska Lane</p>
        <p>Ravipur</p>
        <p>Ostavia</p>
      </address>
    </div>
    <p class="website">vortani-example.com</p>
  </article>

  <article class="card brand">
    <div class="brand-mark">
      <span class="brand-dot"></span>
      <h1 class="brand-name">VORTANI</h1>
    </div>
    <p class="field-title">OUR WORKING FIELD:</p>
    <div class="field-list">
      <p>Private Labeling<span class="sep">•</span>high Quality Production<span class="sep">•</span>direct distribution</p>
      <p>warehousing<span class="sep">•</span>trademark registration<span class="sep">•</span>legal support</p>
    </div>
  </article>
</main>
</body>
</html>
```